Financial planning firm needs business card designed

Hello

I am looking to have a standard size business card designed for our agents. Attached is our logo.

Industry/Entity Type

Financial Service

Requirements
Must have
• Marcus Pellow
• Mortgage Agent
• Investment Specialist
• Office Address: 7 Bramble Ave. W., Suite K300, Hamilton, ON L9K 2R6
• Office Ph#: (905) 555-0148 x 317
• email: mpellow@corvantifg.com
• www.corvantifg.com
• TLRA Lic# 40513
Nice to have
• On the back maybe put:
• 8% to 12% Fixed per year! Ask me how.

```html
<!DOCTYPE html>
<html lang="en">
<head>
<meta charset="utf-8">
<title>Corvanti Financial Group – Business Card</title>
<link rel="stylesheet" href="https://fonts.googleapis.com/css2?family=Cinzel:wght@400&family=Marcellus+SC&family=Open+Sans:wght@400;700&display=swap">
<style>
  :root {
    --backdrop: #d1d2d4;
    --card: #2f2a33;
    --panel: #1b181d;
    --teal: #53c4b3;
    --white: #ffffff;
    --shadow: rgba(0,0,0,0.35);
  }
  * { margin: 0; padding: 0; box-sizing: border-box; }
  html, body { width: 1200px; height: 1000px; overflow: hidden; }
  body { background: var(--backdrop); position: relative; font-family: "Open Sans", sans-serif; }

  .card {
    position: absolute; top: 166px; width: 392px; height: 668px;
    background: var(--card); overflow: hidden;
    box-shadow: 4px 5px 6px var(--shadow);
  }
  .card--front { left: 182px; }
  .card--back { left: 627px; width: 391px; }

  .brand { position: absolute; left: 0; right: 0; text-align: center; }
  .brand__mark {
    display: block; margin: 0 auto; width: 58px; height: 58px; background: var(--teal);
  }
  .brand__name {
    display: block; margin-top: 22px;
    font-family: "Cinzel", serif; font-weight: 400; font-size: 23px;
    letter-spacing: 1px; color: var(--white); white-space: nowrap;
  }
  .card--front .brand { top: 66px; }
  .card--back .brand { top: 76px; }

  .agent { position: absolute; top: 192px; left: 0; right: 0; text-align: center; font-family: "Marcellus SC", serif; }
  .agent__name { color: var(--teal); font-size: 35px; line-height: 1; letter-spacing: 1px; }
  .agent__title { color: var(--white); font-size: 25px; line-height: 1; margin-top: 6px; letter-spacing: 1px; }

  .contact-panel {
    position: absolute; left: 58px; top: 282px; width: 276px; height: 400px;
    background: var(--panel); border: 2px solid var(--teal);
  }
  .contact-list { list-style: none; position: absolute; left: 0; right: 0; top: 33px; text-align: center; color: var(--white); font-size: 15.5px; line-height: 23px; }
  .contact-item { position: absolute; left: 0; right: 0; }
  .contact-item svg { display: block; margin: 0 auto 6px; width: 22px; height: 22px; }
  .contact-item--address { top: 0; }
  .contact-item--phone { top: 88px; }
  .contact-item--email { top: 153px; }
  .contact-item--web { top: 218px; }
  .contact-item--licence { top: 283px; }

  .offer-panel {
    position: absolute; left: 85px; top: 287px; width: 221px; height: 253px;
    background: var(--panel); border: 2px solid var(--teal);
    text-align: center; font-weight: 700;
  }
  .offer__rate { margin-top: 73px; color: var(--teal); font-size: 27px; line-height: 32px; }
  .offer__rate small { color: var(--white); font-size: 18px; }
  .offer__fixed { color: var(--white); font-size: 18px; line-height: 26px; }
  .offer__cta { color: var(--teal); font-size: 22px; line-height: 30px; }
</style>
</head>
<body>

<section class="card card--front" aria-label="Business card front">
  <div class="brand">
    <span class="brand__mark"></span>
    <span class="brand__name">CORVANTI FINANCIAL GROUP</span>
  </div>

  <div class="agent">
    <p class="agent__name">Marcus Pellow</p>
    <p class="agent__title">Mortgage Agent</p>
  </div>

  <div class="contact-panel">
    <ul class="contact-list">
      <li class="contact-item contact-item--address">
        <svg viewBox="0 0 22 22" aria-hidden="true"><circle cx="11" cy="11" r="11" fill="#53c4b3"/><path d="M11 4.5a4 4 0 0 0-4 4c0 3 4 8 4 8s4-5 4-8a4 4 0 0 0-4-4z" fill="#1b181d"/><circle cx="11" cy="8.5" r="1.5" fill="#53c4b3"/></svg>
        7 Bramble Ave. W., Suite K300,<br>Hamilton, ON L9K 2R6
      </li>
      <li class="contact-item contact-item--phone">
        <svg viewBox="0 0 22 22" aria-hidden="true"><circle cx="11" cy="11" r="11" fill="#53c4b3"/><path d="M14.5 5.5l2 2-1.2 1.2-2-2zM12.8 7.2l2 2-6 6-2.5.6.6-2.5z" fill="#1b181d"/></svg>
        (905) 555-0148 x 317
      </li>
      <li class="contact-item contact-item--email">
        <svg viewBox="0 0 22 22" aria-hidden="true"><circle cx="11" cy="11" r="11" fill="#53c4b3"/><rect x="5.5" y="7" width="11" height="8" fill="#1b181d"/><path d="M5.5 7l5.5 4.5L16.5 7" fill="none" stroke="#53c4b3" stroke-width="1.2"/></svg>
        mpellow@corvantifg.com
      </li>
      <li class="contact-item contact-item--web">
        <svg viewBox="0 0 22 22" aria-hidden="true"><circle cx="11" cy="11" r="11" fill="#53c4b3"/><path d="M5.5 7.5l2 7 2-5.5 1.5 0 2 5.5 2-7" fill="none" stroke="#1b181d" stroke-width="1.8" stroke-linejoin="round"/></svg>
        www.corvantifg.com
      </li>
      <li class="contact-item contact-item--licence">
        <svg viewBox="0 0 22 22" aria-hidden="true"><circle cx="11" cy="11" r="11" fill="#53c4b3"/><rect x="5" y="7.5" width="12" height="7" rx="1.5" fill="#1b181d"/></svg>
        TLRA Lic# 40513
      </li>
    </ul>
  </div>
</section>

<section class="card card--back" aria-label="Business card back">
  <div class="brand">
    <span class="brand__mark"></span>
    <span class="brand__name">CORVANTI FINANCIAL GROUP</span>
  </div>

  <div class="offer-panel">
    <p class="offer__rate">8% <small>to</small>12%</p>
    <p class="offer__fixed">Fixed per year!</p>
    <p class="offer__cta">Ask me how.</p>
  </div>
</section>

</body>
</html>
```